Kelvora

I ran out of business cards I designed myself on line. THe company went out of business and I LOVE my card. I am hoping someone can recreate the look or something equally as appealing to me.

Industry/Entity Type

Business

Colors
ecdaeb
f7f1f7

Requirements
Must have
• The card is going to be printed by a company Taroq.com. they are very high end stock and I market to high end clients…the logo needs to remain small and centered at the top. If it helps my web site is kelvora.net you can see there how I left the logo very small

```html
<!DOCTYPE html>
<html lang="en">
<head>
<meta charset="utf-8">
<title>Kelvora, LLC — Business Card</title>
<link rel="stylesheet" href="https://fonts.googleapis.com/css2?family=Cinzel:wght@400;500&display=swap">
<style>
  :root {
    --page: #ffffff;
    --card-edge: #f7f1f7;
    --card-face: #ecdaeb;
    --ink: #6e3a2c;
  }
  html, body {
    margin: 0;
    padding: 0;
    width: 1000px;
    height: 1200px;
    overflow: hidden;
    background: var(--page);
  }
  .canvas {
    position: relative;
    width: 1000px;
    height: 1200px;
    font-family: "Cinzel", "Times New Roman", serif;
    color: var(--ink);
  }
  .card-edge {
    position: absolute;
    left: 176px;
    top: 68px;
    width: 650px;
    height: 1063px;
    background: var(--card-edge);
  }
  .card-face {
    position: absolute;
    left: 196px;
    top: 88px;
    width: 610px;
    height: 1023px;
    background: var(--card-face);
  }
  .line {
    position: absolute;
    left: 0;
    width: 100%;
    margin: 0;
    text-align: center;
    white-space: nowrap;
    font-weight: 400;
  }
  .brand-mark {
    top: 224px;
    font-size: 46px;
    letter-spacing: 6px;
    line-height: 1;
  }
  .company {
    top: 498px;
    font-size: 60px;
    letter-spacing: 5px;
    line-height: 1;
  }
  .tagline {
    top: 614px;
    font-size: 35px;
    letter-spacing: 2px;
    line-height: 1;
  }
  .contact {
    font-size: 31px;
    letter-spacing: 1.5px;
    line-height: 1;
  }
  .contact-name { top: 766px; }
  .contact-phone { top: 830px; }
  .contact-email { top: 900px; }
</style>
</head>
<body>
  <main class="canvas">
    <div class="card-edge"></div>
    <section class="card-face">
      <p class="line brand-mark">KELVORA</p>
      <h1 class="line company">KELVORA, LLC</h1>
      <p class="line tagline">DESIGN &amp; RENOVATION</p>
      <p class="line contact contact-name">MARISOL DUNHAVEN</p>
      <p class="line contact contact-phone">410-555-0148</p>
      <p class="line contact contact-email">MARISOL@KELVORA.NET</p>
    </section>
  </main>
</body>
</html>
```